Design new RK Capital business card 2016

We need a new business card for our company RK Capital Stewardship. We are a niche Alternative Investment Fund Manager based in Chester, in the North West of the UK.We market our services to global institutions such as banks, insurance companies, pension funds, etc. as well as wealthy individuals. Our main markets are Europe (Germany\France\Switzerland), the US and parts of Asia.
The design needs to be in line with existing company branding. Life the assets we deal with, the business card might suggest, "niche\alternative" type of attributes - however, it needs to remain professional, clean and appropriate for our client base.
Our existing business card format with relevant factual information is included, along with logo and branding details.

Target Market(s)

We market our services to global institutions such as banks, insurance companies, pension funds, etc. as well as wealthy individuals.

Industry/Entity Type

Financial Service

Contact Information for Business Card

please see attached pdf for information on existing business card which we should aim to convey on your new design. However:
- the wording "RK Capital Stewardship Ltd is Authorised and Regulated
by the Monetary Oversight Bureau. Registered No. 7139604" should be replaced with , "RK Capital Stewardship Ltd is an Alternative Investment Fund Manager Authorised and Regulated by the Monetary Oversight Bureau. Registered No. 7139604"
- the "reception" word on reverse can be omitted.
- the "retail: www.marbowhill.co.uk" wording can be omitted.
- the QR code is not required in the new version.

Font styles to use
Serif
Sans Serif

Requirements
Must have
• information on current business card, subject to comments provided above.
Nice to have
• Use of areas of solid colour instead of large areas of white space might be nice to experiment with. However, still need to have the general look and feel of the brand as presented on our website www.rkcapfold.co.uk
• If we had space for 3 bullet points describing what we do\who we are, this might be good to try out. e.g. alternative investment fund manager, longevity specialist, founded 1990.
• Also, we have a new tag line, "wisdom built to endure" which might fit nicely somewhere on the business card.
Should not have
• - no QR code
• - should not use all the colours in our logo as it looks very garish! Using one or two colours with black\white etc, seems to work better.

```html
<!DOCTYPE html>
<html lang="en">
<head>
<meta charset="utf-8">
<title>RK Capital Stewardship – Business Card</title>
<link rel="stylesheet" href="https://fonts.googleapis.com/css2?family=Open+Sans:wght@400;700&family=Libre+Baskerville&display=swap">
<style>
  :root{
    --bg:#2b2b2b;
    --card-black:#050505;
    --card-white:#ffffff;
    --blue:#3cb3e6;
    --gold:#bca33a;
    --olive:#8f8336;
    --brown:#6a3a1d;
    --dark-fill:#15161c;
    --ink-light:#f2f2f2;
    --sans:'Open Sans', Arial, sans-serif;
    --serif:'Libre Baskerville', Georgia, serif;
  }
  *{box-sizing:border-box;margin:0;padding:0}
  html,body{width:1200px;height:900px;overflow:hidden;background:var(--bg)}
  .stage{position:relative;width:1200px;height:900px}
  .card{position:absolute;left:250px;width:700px;height:400px;border-radius:26px;overflow:hidden;box-shadow:0 14px 30px rgba(0,0,0,.45)}

  /* Reverse side */
  .card--reverse{top:40px;background:var(--card-black);font-family:var(--sans);text-align:center;color:var(--blue)}
  .reverse__mark{width:64px;height:64px;border-radius:50%;background:var(--gold);margin:46px auto 0}
  .reverse__founded{font-size:15px;margin-top:14px}
  .reverse__name{font-size:27px;font-weight:700;color:var(--gold);letter-spacing:.5px;margin-top:6px}
  .reverse__services{font-size:15px;margin-top:14px}
  .reverse__services .dot{display:inline-block;width:11px;height:11px;border-radius:50%;background:var(--gold);margin:0 6px 0 10px;vertical-align:-1px}
  .reverse__address{font-size:15px;margin-top:8px}
  .reverse__web{font-size:15px;margin-top:6px}
  .reverse__legal{font-size:13px;line-height:1.45;margin-top:22px;padding:0 40px}

  /* Front side */
  .card--front{top:460px;background:var(--card-white)}
  .front__feature{position:absolute;left:330px;top:-120px;width:510px;height:510px;border-radius:50%;background:var(--dark-fill);border:5px solid var(--blue)}
  .front__brand{position:absolute;left:48px;top:140px;width:300px}
  .front__brandmark{width:58px;height:58px;border-radius:50%;background:var(--olive);margin-bottom:18px}
  .front__brandname{font-family:var(--serif);font-size:30px;line-height:1.2;color:var(--brown)}
  .front__tagline{font-family:var(--serif);font-size:17px;color:var(--blue);letter-spacing:.5px;margin-top:14px;text-transform:uppercase;white-space:nowrap}
  .contact{position:absolute;right:40px;top:70px;text-align:right;font-family:var(--sans)}
  .contact__name{font-size:27px;font-weight:700;color:var(--blue);letter-spacing:.5px}
  .contact__role{font-size:15px;color:var(--gold);margin-top:2px}
  .contact__list{list-style:none;margin-top:20px;color:var(--ink-light);font-size:15px;line-height:1.55}
  .contact__list li{display:flex;justify-content:flex-end;align-items:center;gap:10px}
  .contact__list svg{width:15px;height:15px;fill:none;stroke:var(--gold);stroke-width:2}
</style>
</head>
<body>
<div class="stage">

  <section class="card card--reverse">
    <div class="reverse__mark"></div>
    <p class="reverse__founded">Founded 1990.</p>
    <h1 class="reverse__name">RK CAPITAL STEWARDSHIP</h1>
    <p class="reverse__services"><span class="dot"></span>Alternative Investment<span class="dot"></span>Fund Manager<span class="dot"></span>Longevity Specialist</p>
    <p class="reverse__address">4-7 Ashby Yard | Linden Row | Chester | CH2 4QX | UK</p>
    <p class="reverse__web">www.rkcapfold.co.uk</p>
    <p class="reverse__legal">RK Capital Stewardship Ltd is an Alternative Investment Fund Manager Authorised<br>and Regulated by the Monetary Oversight Bureau. Registered No. 7139604</p>
  </section>

  <section class="card card--front">
    <div class="front__feature" role="img" aria-label="Dark mosaic of angular stained-glass shapes filling the circle"></div>
    <div class="front__brand">
      <div class="front__brandmark"></div>
      <p class="front__brandname">RK Capital<br>Stewardship</p>
      <p class="front__tagline">Wisdom built to endure</p>
    </div>
    <div class="contact">
      <h2 class="contact__name">MARTIN HALE</h2>
      <p class="contact__role">Non-Executive Chairman</p>
      <ul class="contact__list">
        <li>+44 (0)1632 960418
          <svg viewBox="0 0 16 16"><path d="M2 6c0-2 2-3 6-3s6 1 6 3l-2 1-1-2H5L4 7z M4 8h8l1 5H3z"/></svg></li>
        <li>+44 (0)7700 900362
          <svg viewBox="0 0 16 16"><rect x="4" y="1.5" width="8" height="13" rx="1.5"/><line x1="7" y1="12" x2="9" y2="12"/></svg></li>
        <li>mhale@rkcapfold.co.uk
          <svg viewBox="0 0 16 16"><rect x="1.5" y="3.5" width="13" height="9" rx="1"/><path d="M1.5 4l6.5 5 6.5-5"/></svg></li>
      </ul>
    </div>
  </section>

</div>
</body>
</html>
```